(2) Graphics for Online Store. Creative Minds Welcome+

Need (2) Different Graphics for an Online Store selling digital goods.

The digital goods are 'Leads' for Business Loan Brokers. The graphic should resemble 'Money' in some creative way.

#1 Aged Business Funding Leads
# 2 'Business Funding Real Time Calls

Preferred Colors: White/Black/Aqua

Examples of each included below. Not looking for replicas. The attached are examples of similar products only. No Clipart Please! Needs to be a Professional Clean Look! Do not replicate or emulate the attached. This is just an example.

```html
<!DOCTYPE html>
<html lang="en">
<head>
<meta charset="utf-8">
<title>Business Lead Store Graphics</title>
<link rel="stylesheet" href="https://fonts.googleapis.com/css2?family=League+Spartan:wght@700;800&family=Oswald:wght@500;600&display=swap">
<style>
  :root {
    --white: #ffffff;
    --black: #05101a;
    --aqua: #08d2f2;
    --aqua-deep: #0aa0d8;
    --yellow: #fff200;
    --yellow-deep: #ffb400;
    --navy: #1a1444;
    --teal-bg-a: #1f4a5c;
    --teal-bg-b: #0b1e28;
    --purple-bg-a: #4a3a78;
    --purple-bg-b: #2d2456;
    --ink-purple: #22124a;
  }
  * { margin: 0; padding: 0; box-sizing: border-box; }
  html, body { width: 990px; height: 1200px; overflow: hidden; background: var(--white); }
  body { position: relative; font-family: "League Spartan", "Montserrat", sans-serif; }

  .banner { position: absolute; left: 45px; width: 906px; height: 504px; overflow: hidden; }
  .banner--aged { top: 66px; }
  .banner--calls { top: 616px; width: 902px; height: 500px; }

  .backdrop { position: absolute; inset: 0; }
  .banner--aged .backdrop { background: radial-gradient(ellipse at 40% 40%, var(--teal-bg-a), var(--teal-bg-b) 85%); }
  .banner--calls .backdrop { background: radial-gradient(ellipse at 55% 45%, var(--purple-bg-a), var(--purple-bg-b) 90%); }

  .art { position: absolute; }
  .art--cash-hand { left: 530px; top: 180px; width: 376px; height: 324px;
    background: radial-gradient(ellipse at 60% 60%, #d9d9cf 0%, #a9ab9f 45%, rgba(40,30,30,0.9) 80%, rgba(20,20,20,0) 100%); }
  .art--banking { left: 492px; top: 150px; width: 410px; height: 350px;
    background: radial-gradient(ellipse at 60% 55%, rgba(60,170,255,0.75) 0%, rgba(80,70,200,0.55) 45%, rgba(45,36,86,0) 80%); }

  .line { position: absolute; left: 55px; line-height: 1; white-space: nowrap; font-weight: 800; }
  .line--commission { top: 47px; font-size: 80px; color: var(--white); letter-spacing: -1px; }
  .line--money { top: 114px; left: 54px; font-size: 134px; letter-spacing: 6px;
    background: linear-gradient(180deg, var(--aqua) 40%, var(--aqua-deep)); -webkit-background-clip: text; background-clip: text; color: transparent; }
  .line--waiting, .line--found { font-size: 74px;
    background: linear-gradient(180deg, var(--yellow) 45%, var(--yellow-deep)); -webkit-background-clip: text; background-clip: text; color: transparent; }
  .line--waiting { top: 248px; left: 40px; letter-spacing: 0.5px; }
  .line--found { top: 308px; left: 48px; letter-spacing: 3px; }

  .lead-pill { position: absolute; left: 39px; top: 402px; width: 514px; height: 62px;
    background: linear-gradient(180deg, var(--aqua), var(--aqua-deep)); border-radius: 8px;
    display: flex; align-items: center; padding-left: 10px; }
  .lead-pill__label { font-family: "Oswald", sans-serif; font-weight: 600; font-size: 37px; color: var(--navy); letter-spacing: -0.5px; transform: scaleX(0.86); transform-origin: left center; white-space: nowrap; }
  .lead-pill__count { position: absolute; right: 8px; top: 6px; width: 142px; height: 51px; background: var(--white);
    border-radius: 7px; display: flex; align-items: center; justify-content: center;
    font-family: "Oswald", sans-serif; font-weight: 500; font-size: 36px; color: var(--aqua-deep); }
  .lead-pill__count span { transform: scaleX(0.86); white-space: nowrap; }

  .aged-badge { position: absolute; right: 0; top: 0; width: 330px; height: 178px; }
  .aged-badge__text { position: absolute; right: 45px; text-align: right; line-height: 1; font-weight: 800; }
  .aged-badge__days { top: 39px; font-size: 64px; color: var(--aqua); letter-spacing: -1.5px; }
  .aged-badge__aged { top: 94px; font-size: 58px; color: var(--white); letter-spacing: -1px; }

  .line--business { top: 36px; left: 37px; font-size: 108px; color: var(--white); letter-spacing: -3px; }
  .line--funding { top: 128px; left: 37px; font-size: 122px; color: var(--aqua); letter-spacing: 6px; }

  .realtime-box { position: absolute; left: 39px; top: 235px; width: 345px; height: 73px; background: var(--yellow); border-radius: 9px;
    display: flex; align-items: center; justify-content: center; font-weight: 800; font-size: 70px; color: var(--ink-purple); letter-spacing: -2px; line-height: 1; padding-top: 10px; }
  .line--calls { top: 243px; left: 395px; font-size: 70px; color: var(--yellow); letter-spacing: -1px; }

  .dash-rule { position: absolute; left: 44px; width: 392px; border-top: 3px dashed var(--white); }
  .dash-rule--top { top: 322px; }
  .dash-rule--bottom { top: 427px; }

  .owners-arrow { position: absolute; left: 43px; top: 339px; width: 442px; height: 72px; }
  .owners-arrow__text { position: absolute; left: 43px; top: 21px; font-weight: 800; font-size: 42px; color: var(--ink-purple); letter-spacing: -1.5px; line-height: 1; white-space: nowrap; }

  .call-icon { position: absolute; left: 648px; top: 16px; width: 190px; height: 150px; }
</style>
</head>
<body>

<section class="banner banner--aged">
  <div class="backdrop" role="img" aria-label="Dark teal background of scattered hundred dollar bills"></div>
  <div class="art art--cash-hand" role="img" aria-label="Hand in a suit sleeve holding out a fan of hundred dollar bills"></div>

  <svg class="aged-badge" viewBox="0 0 330 178" aria-hidden="true">
    <path d="M40 0 C-5 40 -5 130 60 165 C120 195 230 175 330 145 L330 0 Z" fill="var(--black)"/>
    <path d="M40 0 C-5 40 -5 130 60 165 C120 195 230 175 330 145" fill="none" stroke="var(--yellow)" stroke-width="5"/>
  </svg>
  <div class="aged-badge__text aged-badge__days">10+DAYS</div>
  <div class="aged-badge__text aged-badge__aged">AGED</div>

  <h1 class="line line--commission">COMMISSION</h1>
  <div class="line line--money">MONEY</div>
  <div class="line line--waiting">JUST WAITING</div>
  <div class="line line--found">TO BE FOUND</div>

  <div class="lead-pill">
    <span class="lead-pill__label">AGED BUSINESS LOAN LEADS</span>
    <div class="lead-pill__count"><span>100 LEADS</span></div>
  </div>
</section>

<section class="banner banner--calls">
  <div class="backdrop" role="img" aria-label="Purple background of scattered dollar bills"></div>
  <div class="art art--banking" role="img" aria-label="Glowing mobile banking app with security shield, lock and gold coins"></div>

  <svg class="call-icon" viewBox="0 0 190 150" aria-hidden="true">
    <circle cx="70" cy="70" r="67" fill="var(--ink-purple)" stroke="var(--aqua)" stroke-width="2"/>
    <circle cx="156" cy="109" r="13" fill="none" stroke="var(--aqua)" stroke-width="2"/>
    <circle cx="180" cy="133" r="7" fill="none" stroke="var(--aqua)" stroke-width="2"/>
    <path d="M38 44 L52 34 L66 54 L58 62 C62 74 72 84 84 88 L92 80 L110 94 L100 108 C70 108 38 78 38 44 Z"
          fill="none" stroke="var(--yellow)" stroke-width="5" stroke-linejoin="round"/>
    <path d="M78 36 A28 28 0 0 1 106 64" fill="none" stroke="var(--yellow)" stroke-width="5" stroke-linecap="round"/>
    <path d="M78 20 A44 44 0 0 1 122 64" fill="none" stroke="var(--yellow)" stroke-width="5" stroke-linecap="round"/>
  </svg>

  <h1 class="line line--business">BUSINESS</h1>
  <div class="line line--funding">FUNDING</div>
  <div class="realtime-box">REAL TIME</div>
  <div class="line line--calls">CALLS</div>

  <div class="dash-rule dash-rule--top"></div>
  <div class="owners-arrow">
    <svg width="442" height="72" viewBox="0 0 442 72" aria-hidden="true">
      <defs>
        <linearGradient id="arrowFill" x1="0" y1="0" x2="0" y2="1">
          <stop offset="0" stop-color="var(--aqua)"/>
          <stop offset="1" stop-color="var(--aqua-deep)"/>
        </linearGradient>
      </defs>
      <path d="M0 0 L386 0 L414 36 L386 72 L0 72 L36 36 Z" fill="url(#arrowFill)"/>
      <path d="M396 0 L412 0 L442 36 L412 72 L396 72 L426 36 Z" fill="var(--aqua)"/>
    </svg>
    <div class="owners-arrow__text">TALK TO OWNERS</div>
  </div>
  <div class="dash-rule dash-rule--bottom"></div>
</section>

</body>
</html>
```